Graphic of Teacher Agility Framework

I need a model designed for my teacher educator agility framework. The concepts are responsive to each other on Figure 12 on the attachment and the text explains it all.

This is meant to be a conceptual framework of how ones thinks between experience, and theory, and research.

The domains represent a hierarchy of knowledge of specific domains that have enabled my learning to develop in-depth. I chose the term ‘agility framework’ to emphasise the importance of a responsiveness to the context and of the ability to respond with urgency between the various components (The Quillmark, 2012). I present the agility framework in Figure 12. The concentric circles are inter-connected as they are inter-dependent aspects of developing personal empowerment. The applicability of each domain relies on my ability to be aware of the context and to build work with urgency.

My learning has been iterative throughout this research, so this framework is intended to be understood as iterative, with movement between the concentric circles at a cognitive and behavioural level when greater awareness is gained. At the heart of the main circle are the researcherly dispositions that have been essential to my research and professional roles as well as to my personal learning. I have used descriptive headings for these dispositions that I believe are helpful for understanding them. The first one, ‘value deep understanding’, is modelled on Vostrup (2019); whilst ‘cognitive flexibility’ is an inter-cultural competency from Brasko et al (2014). I have also added in ‘responsiveness’ and ‘sensory awareness’ which I believe are additional dispositions that have emerged in this study. Whilst conducting this research I have been responsive to the context, the participants, and the data, whilst gaining a greater awareness of my place within UAE society.

Target Market(s)

Academic, research

Requirements
Must have
• Attractive Visuals
Nice to have
• Connections between the concepts

```html
<!DOCTYPE html>
<html lang="en">
<head>
<meta charset="utf-8">
<title>Learning Agility Framework</title>
<link rel="stylesheet" href="https://fonts.googleapis.com/css2?family=Source+Sans+3:wght@400;700&display=swap">
<style>
  :root {
    --paper: #ffffff;
    --ring: #c4c4c4;
    --accent: #f7003f;
    --ink: #555a5c;
    --ink-strong: #4a4f51;
  }
  html, body { margin: 0; padding: 0; overflow: hidden; background: var(--paper); }
  .canvas { width: 1200px; height: 1000px; display: block; }
  .label { font-family: "Source Sans 3", "Myriad Pro", sans-serif; font-size: 10.5px; fill: var(--ink); text-anchor: middle; }
  .label-strong { font-family: "Source Sans 3", "Myriad Pro", sans-serif; font-size: 12.5px; font-weight: 700; fill: var(--ink-strong); text-anchor: middle; }
  .title { font-family: "Source Sans 3", "Myriad Pro", sans-serif; font-size: 20px; font-weight: 700; fill: var(--ink-strong); text-anchor: middle; }
  .ring { fill: none; stroke: var(--ring); }
  .disc { fill: var(--ring); }
  .halo { fill: var(--paper); }
  .cut { stroke: var(--paper); stroke-linecap: butt; }
  .link { stroke: var(--accent); stroke-width: 1.2; fill: none; }
</style>
</head>
<body>
<svg class="canvas" viewBox="0 0 1200 1000" xmlns="http://www.w3.org/2000/svg">
  <defs>
    <marker id="arrow-tip" viewBox="0 0 10 10" refX="9" refY="5" markerWidth="6" markerHeight="6" orient="auto-start-reverse">
      <path d="M1,1 L9,5 L1,9" fill="none" stroke="#f7003f" stroke-width="1.4"/>
    </marker>
    <path id="arc-research" d="M 503,454 A 97 97 0 0 1 697,454"/>
  </defs>

  <!-- outer environment ring -->
  <circle class="ring" cx="600" cy="454" r="240.5" stroke-width="59"/>

  <!-- halos around external factors and personal empowerment -->
  <circle class="halo" cx="517" cy="209" r="57"/>
  <circle class="halo" cx="726" cy="227" r="57"/>
  <circle class="halo" cx="354" cy="376" r="57"/>
  <circle class="halo" cx="378" cy="585" r="57"/>
  <circle class="halo" cx="953" cy="457" r="148"/>

  <!-- external factors -->
  <g class="factor">
    <circle class="disc" cx="517" cy="209" r="42"/>
    <text class="label" x="518" y="206">cultural</text>
    <text class="label" x="518" y="218">differences</text>
  </g>
  <g class="factor">
    <circle class="disc" cx="726" cy="227" r="42"/>
    <text class="label" x="726" y="226">employment</text>
    <text class="label" x="726" y="238">contacts</text>
  </g>
  <g class="factor">
    <circle class="disc" cx="354" cy="376" r="42"/>
    <text class="label" x="355" y="376">education</text>
    <text class="label" x="355" y="388">regulations</text>
  </g>
  <g class="factor">
    <circle class="disc" cx="378" cy="585" r="42"/>
    <text class="label" x="378" y="589">macro economic</text>
    <text class="label" x="378" y="601">factore</text>
  </g>

  <!-- context / relationships ring -->
  <circle class="ring" cx="600" cy="454" r="163" stroke-width="50"/>
  <line class="cut" x1="693" y1="361" x2="743" y2="311" stroke-width="12"/>
  <line class="cut" x1="507" y1="547" x2="457" y2="597" stroke-width="12"/>

  <!-- consumption of research ring -->
  <circle class="ring" cx="600" cy="454" r="110" stroke-width="28"/>

  <!-- dispositions core -->
  <circle class="disc" cx="600" cy="454" r="66"/>
  <line class="cut" x1="550" y1="404" x2="650" y2="504" stroke-width="7"/>
  <line class="cut" x1="650" y1="404" x2="550" y2="504" stroke-width="7"/>
  <circle class="halo" cx="600" cy="454" r="12"/>
  <circle cx="600" cy="454" r="73" fill="none" stroke="var(--accent)" stroke-width="10"
          stroke-linecap="round" stroke-dasharray="90.7 24" stroke-dashoffset="-69.3"/>

  <text class="label" x="600" y="404">value deep</text>
  <text class="label" x="600" y="416">understanding</text>
  <text class="label" x="559" y="451">sensory</text>
  <text class="label" x="559" y="463">awareness</text>
  <text class="label" x="641" y="451">cognitive</text>
  <text class="label" x="641" y="463">flexibility</text>
  <text class="label" x="600" y="505">responsiveness</text>

  <!-- ring labels -->
  <text class="label"><textPath href="#arc-research" startOffset="52%">consumption of research</textPath></text>
  <text class="label" transform="translate(494,335) rotate(-42)">context</text>
  <text class="label" transform="translate(711,573) rotate(-47)">relationships</text>
  <text class="label" transform="translate(752,629) rotate(-45)">inter-cultural competence</text>

  <!-- outer qualities -->
  <text class="label-strong" transform="translate(834,627) rotate(-62)">reflexivity</text>
  <text class="label-strong" transform="translate(749,697) rotate(-31)">awareness of self</text>
  <text class="label-strong" transform="translate(650,737) rotate(-9)">urgency</text>
  <text class="label-strong" transform="translate(573,742) rotate(4)">speed</text>
  <text class="label-strong" transform="translate(504,725) rotate(18)">time</text>

  <!-- connections -->
  <line class="link" x1="528" y1="254" x2="532" y2="272" marker-start="url(#arrow-tip)" marker-end="url(#arrow-tip)"/>
  <line class="link" x1="536" y1="252" x2="540" y2="270" marker-start="url(#arrow-tip)" marker-end="url(#arrow-tip)"/>
  <line class="link" x1="689" y1="283" x2="698" y2="266" marker-start="url(#arrow-tip)" marker-end="url(#arrow-tip)"/>
  <line class="link" x1="696" y1="288" x2="705" y2="271" marker-start="url(#arrow-tip)" marker-end="url(#arrow-tip)"/>
  <line class="link" x1="400" y1="383" x2="420" y2="388" marker-start="url(#arrow-tip)" marker-end="url(#arrow-tip)"/>
  <line class="link" x1="398" y1="391" x2="418" y2="396" marker-start="url(#arrow-tip)" marker-end="url(#arrow-tip)"/>
  <line class="link" x1="417" y1="558" x2="435" y2="548" marker-start="url(#arrow-tip)" marker-end="url(#arrow-tip)"/>
  <line class="link" x1="421" y1="566" x2="439" y2="556" marker-start="url(#arrow-tip)" marker-end="url(#arrow-tip)"/>
  <line class="link" x1="799" y1="447" x2="827" y2="447" marker-start="url(#arrow-tip)" marker-end="url(#arrow-tip)"/>
  <line class="link" x1="799" y1="460" x2="827" y2="460" marker-start="url(#arrow-tip)" marker-end="url(#arrow-tip)"/>

  <!-- personal empowerment -->
  <g class="empowerment">
    <text class="label-strong" x="953" y="243">personal</text>
    <text class="label-strong" x="953" y="258">empowerment</text>
    <line x1="953" y1="272" x2="953" y2="347" stroke="var(--ring)" stroke-width="3"/>
    <circle cx="953" cy="272" r="6" fill="var(--ring)"/>

    <circle class="ring" cx="953" cy="457" r="82" stroke-width="58"/>
    <line class="cut" x1="910" y1="414" x2="870" y2="374" stroke-width="12"/>
    <line class="cut" x1="996" y1="414" x2="1036" y2="374" stroke-width="12"/>
    <line class="cut" x1="910" y1="500" x2="870" y2="540" stroke-width="12"/>
    <line class="cut" x1="996" y1="500" x2="1036" y2="540" stroke-width="12"/>

    <circle cx="953" cy="457" r="37.5" fill="none" stroke="var(--accent)" stroke-width="1.3"/>
    <polyline points="979,427 983,438 990,431" fill="none" stroke="var(--accent)" stroke-width="1.3"/>
    <polyline points="915,478 923,482 917,489" fill="none" stroke="var(--accent)" stroke-width="1.3"/>

    <text class="label" x="953" y="376">agency</text>
    <text class="label" x="1033" y="460">tension</text>
    <text class="label" x="953" y="535">personal</text>
    <text class="label" x="953" y="547">growth</text>
    <text class="label" x="871" y="460">tacit</text>
    <text class="label" x="871" y="472">knowledge</text>
  </g>

  <text class="title" x="600" y="867">Learning Agility Framework</text>
</svg>
</body>
</html>
```